"End of year wishes" - Electronic card

Quenlax is a regulatory consulting company in the cosmetic sector. We provide premium services and have 12 years of experience.
Please visit our website for more information: https://quenlax.example
Like every year, we would like to send an electronic design to our clients and partners to wish them happy holidays. This year, we would like to share two good news with them: offer them a surprise (to be revealed later on) and invite them to visit our new brand new website. We relay on your talent and imagination for the design! We need something very professional, serious, beautiful and in line with our graphic layout (see our company website)

Target Market(s)

cosmetic brands

Industry/Entity Type

Cosmetics

Requirements
Must have
• The following statement should be included to the design:

We wish you a Happy Holiday and a Marvelous New Year 2021!
As December is the month of giving, we have a surprise for you. Please contact your dedicated Account Manager to find out more!

Good news never comes alone, we've also updated our website in order to serve you better. We hope you like it as much as we do.
Please enjoy the experience: www.quenlax.example

```html
<!DOCTYPE html>
<html lang="en">
<head>
<meta charset="utf-8">
<title>Quenlax – Happy Holidays</title>
<link rel="stylesheet" href="https://fonts.googleapis.com/css2?family=Kaushan+Script&family=Montserrat:wght@400;500;700&display=swap">
<style>
  :root {
    --sky-light: #d6ecf6;
    --sky: #bfe0ef;
    --sky-deep: #a9d3e8;
    --leaf-green: #8cab3a;
    --ink: #1f1f1f;
    --ink-soft: #2b2b2b;
    --tree-light: #e4e7e6;
    --tree-gold: #d9c9a3;
  }
  html, body {
    margin: 0;
    padding: 0;
    overflow: hidden;
  }
  .card {
    position: relative;
    width: 1200px;
    height: 800px;
    overflow: hidden;
    background: radial-gradient(ellipse at 70% 30%, var(--sky-light) 0%, var(--sky) 60%, var(--sky-deep) 100%);
    font-family: "Montserrat", sans-serif;
    color: var(--ink);
  }
  .cosmetics-tree {
    position: absolute;
    left: 95px;
    top: 95px;
    width: 370px;
    height: 610px;
  }
  .greeting__line {
    position: absolute;
    left: 476px;
    width: 700px;
    margin: 0;
    text-align: center;
    line-height: 1;
    white-space: nowrap;
  }
  .greeting__lead {
    top: 98px;
    font-size: 32px;
    font-weight: 400;
  }
  .greeting__bridge {
    top: 256px;
    font-size: 31px;
    font-weight: 400;
  }
  .greeting__bridge strong { font-weight: 700; letter-spacing: 0.5px; }
  .greeting__script {
    font-family: "Kaushan Script", cursive;
    color: var(--leaf-green);
    font-weight: 400;
  }
  .greeting__script--holidays {
    top: 134px;
    left: 466px;
    font-size: 88px;
  }
  .greeting__script--year {
    top: 296px;
    left: 456px;
    font-size: 110px;
  }
  .message {
    position: absolute;
    left: 520px;
    width: 612px;
    top: 440px;
    text-align: center;
    font-size: 18px;
    line-height: 23px;
    color: var(--ink-soft);
  }
  .message p { margin: 0 0 24px; }
  .message__link { font-weight: 700; color: var(--ink); text-decoration: none; }
  .brand-name {
    position: absolute;
    left: 666px;
    width: 320px;
    top: 658px;
    margin: 0;
    text-align: center;
    font-family: "Montserrat", sans-serif;
    font-weight: 700;
    font-size: 50px;
    line-height: 1.1;
    letter-spacing: 1px;
    color: var(--ink-soft);
  }
</style>
</head>
<body>
  <main class="card">
    <svg class="cosmetics-tree" viewBox="0 0 370 610" role="img" aria-label="Christmas tree arranged from makeup products, perfume bottle, gold baubles and stars, topped with a golden snowflake">
      <defs>
        <linearGradient id="treeTone" x1="0" y1="0" x2="0" y2="1">
          <stop offset="0" stop-color="var(--tree-gold)" stop-opacity="0.55"/>
          <stop offset="1" stop-color="var(--tree-light)" stop-opacity="0.75"/>
        </linearGradient>
      </defs>
      <polygon points="185,0 370,610 0,610" fill="url(#treeTone)"/>
    </svg>

    <header class="greeting">
      <p class="greeting__line greeting__lead">We wish you</p>
      <h1 class="greeting__line greeting__script greeting__script--holidays">Happy Holidays</h1>
      <p class="greeting__line greeting__bridge">and a <strong>MARVELOUS</strong></p>
      <h2 class="greeting__line greeting__script greeting__script--year">New Year!</h2>
    </header>

    <section class="message">
      <p>As December is the month of giving, we have a surprise for you.<br>
      Please contact your dedicated Account Manager to<br>
      find out more!</p>
      <p>Good news never comes alone, we've also updated our website in<br>
      order to serve you better. We hope you like it as much as we do.</p>
      <p>Please enjoy the experience: <a class="message__link" href="https://quenlax.example">www.quenlax.example</a></p>
    </section>

    <p class="brand-name">quenlax</p>
  </main>
</body>
</html>
```